Book cover for ebook and Physical book for Mind Clutter Collective

I run a non-profit Mind Clutter Collective and I have a new book that needs a cover. For the physical book, I will need a full wrap. The mission is to help individuals Quiet the cycle of restless worry patterns. This book is title is "Quiet the cycle of restless worry patterns", and subtitle "Clear Your Mind of Static Noise." I am open to anything design wise, nothing is set in stone. Oh, MCC is pending Trademark.

Target Market(s)

Typically it's Mom's from 25-40

Industry/Entity Type

Mental Health

Font styles to use
Serif

Colors
f37122
9bcb3b
fbed22
0255a3
e34197

Requirements
Must have
• I do like simplicity, yet vibrant colors.
Nice to have
• The authors are Rex T. Whitford, and Dana Okonkwo. For some inspiration individuals refer to me as the Wonder Guide having reversed five incurable diseases.
Should not have
• The cover shouldn't be too busy.

```html
<!DOCTYPE html>
<html lang="en">
<head>
<meta charset="utf-8">
<title>Quiet the Cycle of Restless Worry Patterns — Cover Wrap</title>
<link rel="stylesheet" href="https://fonts.googleapis.com/css2?family=Amatic+SC:wght@700&family=Josefin+Sans:wght@400&family=Caveat+Brush&display=swap">
<style>
  :root {
    --backdrop: #efefef;
    --paper: #ffffff;
    --ink: #1f1f1f;
    --spine-blue: #3f93d1;
    --band-blue: #3d96d0;
    --band-teal: #2fb5a0;
    --band-red: #e2505e;
    --band-yellow: #f7bf45;
    --band-peach: #f4ad9a;
    --title-white: #ffffff;
  }
  html, body {
    margin: 0;
    width: 1200px;
    height: 1200px;
    overflow: hidden;
    background: var(--backdrop);
  }
  .cover-wrap {
    position: absolute;
    left: 209px;
    top: 60px;
    width: 782px;
    height: 1080px;
    background: var(--paper);
    box-shadow: 0 2px 10px rgba(0,0,0,0.08);
  }
  .cover-wrap svg { display: block; }
  .author-line {
    font-family: "Josefin Sans", sans-serif;
    font-size: 25px;
    letter-spacing: 4px;
    fill: var(--ink);
  }
  .spine-author {
    font-family: "Josefin Sans", sans-serif;
    font-size: 17px;
    letter-spacing: 3px;
    fill: var(--ink);
  }
  .spine-mark {
    font-family: "Josefin Sans", sans-serif;
    font-size: 11px;
    fill: var(--ink);
  }
  .spine-title {
    font-family: "Amatic SC", sans-serif;
    font-weight: 700;
    font-size: 34px;
    fill: var(--title-white);
  }
  .title-word {
    font-family: "Amatic SC", sans-serif;
    font-weight: 700;
    fill: var(--title-white);
  }
  .title-word--lg { font-size: 200px; }
  .title-word--md { font-size: 170px; }
  .title-word--sm { font-size: 160px; }
  .title-small {
    font-family: "Amatic SC", sans-serif;
    font-weight: 700;
    font-size: 58px;
    fill: var(--title-white);
  }
  .subtitle {
    font-family: "Caveat Brush", cursive;
    font-size: 44px;
    fill: var(--ink);
  }
</style>
</head>
<body>
  <div class="cover-wrap">
    <svg width="782" height="1080" viewBox="0 0 782 1080" xmlns="http://www.w3.org/2000/svg">
      <defs>
        <linearGradient id="wash-blue" x1="0" x2="1">
          <stop offset="0" stop-color="var(--band-blue)" stop-opacity="0.95"/>
          <stop offset="0.6" stop-color="var(--band-blue)" stop-opacity="0.8"/>
          <stop offset="1" stop-color="var(--band-blue)" stop-opacity="0.95"/>
        </linearGradient>
        <linearGradient id="wash-teal" x1="0" x2="1">
          <stop offset="0" stop-color="var(--band-teal)" stop-opacity="0.95"/>
          <stop offset="0.6" stop-color="var(--band-teal)" stop-opacity="0.75"/>
          <stop offset="1" stop-color="var(--band-teal)" stop-opacity="0.9"/>
        </linearGradient>
        <linearGradient id="wash-red" x1="0" x2="1">
          <stop offset="0" stop-color="var(--band-red)" stop-opacity="0.95"/>
          <stop offset="0.6" stop-color="var(--band-red)" stop-opacity="0.75"/>
          <stop offset="1" stop-color="var(--band-red)" stop-opacity="0.9"/>
        </linearGradient>
        <linearGradient id="wash-yellow" x1="0" x2="1">
          <stop offset="0" stop-color="var(--band-yellow)" stop-opacity="0.9"/>
          <stop offset="0.6" stop-color="var(--band-yellow)" stop-opacity="0.75"/>
          <stop offset="1" stop-color="var(--band-yellow)" stop-opacity="0.9"/>
        </linearGradient>
        <linearGradient id="wash-peach" x1="0" x2="1">
          <stop offset="0" stop-color="var(--band-peach)" stop-opacity="0.9"/>
          <stop offset="0.6" stop-color="var(--band-peach)" stop-opacity="0.7"/>
          <stop offset="1" stop-color="var(--band-peach)" stop-opacity="0.9"/>
        </linearGradient>
      </defs>

      <g class="spine">
        <rect x="0" y="356" width="82" height="724" fill="var(--spine-blue)"/>
        <g transform="translate(0,82) rotate(90)">
          <text class="spine-author" x="0" y="-42">REX T. WHITFORD</text>
          <text class="spine-author" x="0" y="-20">DANA OKONKWO</text>
        </g>
        <circle cx="40" cy="306" r="9" fill="none" stroke="var(--ink)" stroke-width="2"/>
        <text class="spine-mark" x="40" y="334" text-anchor="middle">MCC</text>
        <text class="spine-title" transform="translate(30,376) rotate(90)" textLength="680" lengthAdjust="spacingAndGlyphs">QUIET THE CYCLE OF RESTLESS WORRY PATTERNS</text>
      </g>

      <g class="front">
        <text class="author-line" x="432" y="64" text-anchor="middle">REX T. WHITFORD • DANA OKONKWO</text>

        <g class="title-bands" role="img" aria-label="Watercolour brush-stroke bands in blue, teal, red, yellow and peach behind the title">
          <rect x="100" y="108" width="562" height="184" fill="url(#wash-blue)"/>
          <rect x="104" y="318" width="582" height="158" fill="url(#wash-teal)"/>
          <rect x="104" y="490" width="590" height="150" fill="url(#wash-red)"/>
          <rect x="118" y="652" width="580" height="158" fill="url(#wash-yellow)"/>
          <rect x="112" y="828" width="592" height="148" fill="url(#wash-peach)"/>
        </g>

        <g class="title">
          <text class="title-word title-word--lg" x="140" y="276" textLength="500" lengthAdjust="spacingAndGlyphs">QUIET</text>
          <text class="title-small" transform="translate(112,340) rotate(90)" textLength="110" lengthAdjust="spacingAndGlyphs">THE</text>
          <text class="title-word title-word--md" x="176" y="460" textLength="436" lengthAdjust="spacingAndGlyphs">CYCLE</text>
          <text class="title-small" transform="translate(624,362) rotate(90)" textLength="68" lengthAdjust="spacingAndGlyphs">OF</text>
          <text class="title-word title-word--sm" x="128" y="624" textLength="544" lengthAdjust="spacingAndGlyphs">RESTLESS</text>
          <text class="title-word title-word--md" x="160" y="794" textLength="500" lengthAdjust="spacingAndGlyphs">WORRY</text>
          <text class="title-word title-word--sm" x="134" y="960" textLength="548" lengthAdjust="spacingAndGlyphs">PATTERNS</text>
        </g>

        <text class="subtitle" x="432" y="1036" text-anchor="middle">Clear Your Mind of Static Noise</text>
      </g>
    </svg>
  </div>
</body>
</html>
```